PAcifier/dummy design

Brand - Fable & Fern
Company - Australian designed ethical quality natural range.
Product - natural rubber soother/pacifier/dummy.
Box - 2 dummy's per box.
- hangable in store and stackable on shelf.
- box created with POS stand in mind would be amazing.
- box that is compact and easily ship-able.
- ideas - milk carton - or flat top milk carton style...
- matte finish.
Feel - modern, organic, boutique, clean and simplistic.
Natural product but for the boutique buyer, but can alos be placed in upmarket chemist, quality health food shop or chain store. target is not the hippy natural style, but the modern mama after something clean and quality.
for example - the mum from this page may buy it - https://www.instagram.com/pebbleandlark/
Colours & tones - matte finish.
- black logo
- white, cardboard tone, and soft tones included in the wreath in the images.
- current packaging image included.
Vision - designed in australia - made in Malaysia - exported to the world
Product variations
There are products that are the same but the brand sets them apart....
for example -
Breast feeding biscuits
A = cheap look https://www.instagram.com/mumcrumbsco/
B = quality look https://www.instagram.com/velmaspantry/
Lipgloss
A = cheap https://www.instagram.com/glintara_beauty/
B = quality https://www.instagram.com/dewbycorvell/
Boxes included - kanagroo - I had originally wanted an animal - i have decided to just get a beautiful packaging. simple, modern and lovely. I do like the font used in the kanagroo box tho
The other packaging designs are examples of what I thought - but the tall box will be hard to ship.
Target Market(s)
Baby - Organic natural modern mumma
Stores - premium pharmacies, baby boutiques. Department stores.

```html
<!DOCTYPE html>
<html lang="en">
<head>
<meta charset="utf-8">
<title>Fable &amp; Fern — Natural Rubber Pacifier</title>
<link rel="stylesheet" href="https://fonts.googleapis.com/css2?family=Josefin+Sans:wght@300;400;600&display=swap">
<style>
  :root{
    --sky:#ade6fa;
    --carton-white:#fbfbfb;
    --carton-shade:#eceeef;
    --fold-shade:#e4e7e8;
    --ink:#1d1d22;
    --paper:#ffffff;
  }
  *{margin:0;padding:0;box-sizing:border-box}
  html,body{width:1200px;height:2300px;overflow:hidden;background:var(--sky)}
  .canvas{position:relative;width:1200px;height:2300px;background:var(--sky);font-family:"Josefin Sans",sans-serif;color:var(--ink)}
  .carton{position:absolute;left:301px;top:339px;width:598px;height:1553px}
  .hang-panel{position:absolute;left:0;top:0;width:598px;height:382px;
    background:linear-gradient(90deg,var(--carton-shade) 0%,var(--carton-white) 35%,var(--carton-white) 65%,var(--carton-shade) 100%)}
  .hang-slot{position:absolute;left:247px;top:62px;width:142px;height:58px}
  .fold-band{position:absolute;left:0;top:382px;width:598px;height:73px;
    background:linear-gradient(180deg,var(--fold-shade) 0%,var(--carton-white) 100%)}
  .front-face{position:absolute;left:0;top:455px;width:598px;height:1098px;
    background:linear-gradient(90deg,var(--carton-shade) 0%,var(--carton-white) 30%,var(--paper) 55%,var(--carton-shade) 100%)}
  .motif-pattern{position:absolute;inset:0;
    background:radial-gradient(circle at 30% 40%,rgba(173,230,250,.12),transparent 60%),radial-gradient(circle at 70% 70%,rgba(200,170,220,.10),transparent 60%)}
  .twin-tag{position:absolute;right:0;top:564px;width:163px;height:63px;background:var(--ink);color:var(--paper);
    clip-path:polygon(10% 0,100% 0,100% 100%,0 100%,0 18%);
    display:flex;align-items:center;justify-content:center;font-weight:600;font-size:22px;letter-spacing:1px;padding-top:4px}
  .brand-mark{position:absolute;left:0;width:610px;top:780px;text-align:center;font-weight:400;font-size:58px;letter-spacing:1px}
  .product-frame{position:absolute;left:61px;top:1022px;width:481px;height:201px;border:3px solid var(--ink);
    display:flex;flex-direction:column;align-items:center;justify-content:center;gap:14px}
  .product-material{font-weight:400;font-size:44px;letter-spacing:5px;padding-top:8px}
  .product-name{font-weight:300;font-size:62px;letter-spacing:14px;padding-left:14px}
  .age-badge{position:absolute;left:403px;top:1253px;width:153px;height:153px;border-radius:50%;
    border:5px dotted var(--ink);display:flex;flex-direction:column;align-items:center;justify-content:center}
  .age-range{font-weight:600;font-size:34px;line-height:1;padding-top:6px}
  .age-unit{font-weight:400;font-size:22px;line-height:1.2}
</style>
</head>
<body>
<div class="canvas">
  <div class="carton">
    <div class="hang-panel">
      <div class="motif-pattern" role="img" aria-label="Faint scattered pattern of pacifiers, little birds and baby faces"></div>
      <svg class="hang-slot" viewBox="0 0 142 58" aria-hidden="true">
        <path d="M14 14 H50 C50 2 56 0 71 0 C86 0 92 2 92 14 H128 C136 14 142 20 142 28 V44 C142 52 136 58 128 58 H14 C6 58 0 52 0 44 V28 C0 20 6 14 14 14 Z" fill="var(--sky)"/>
      </svg>
    </div>
    <div class="fold-band"></div>
    <div class="front-face" style="top:455px">
      <div class="motif-pattern" role="img" aria-label="Faint scattered pattern of pacifiers, little birds and baby faces"></div>
    </div>
    <div class="twin-tag">TWIN PACK</div>
    <div class="brand-mark">Fable &amp; Fern</div>
    <div class="product-frame">
      <span class="product-material">NATURAL RUBBER</span>
      <span class="product-name">PACIFIER</span>
    </div>
    <div class="age-badge">
      <span class="age-range">6 | 8</span>
      <span class="age-unit">months</span>
    </div>
  </div>
</div>
</body>
</html>
```